EPS Recycling End Market Infographic

We need a two-page visual presentation of new end-market applications for recycled expanded polystyrene (EPS) collected for recycling. This focuses on expanded polystyrene (foam) transport packaging used for international distribution of goods, including pharmaceuticals and food, electronics, appliances and other products that need superior packaging protection.

The bulletin will have examples of 5 major industry categories that benefit from recycled EPS feedstock for reverse engineering to meet current market demand. It will also showcase names of companies that use recycled content EPS in their product manufacturing to legitimize end market adoption. The capability to use recycled EPS in new EPS packaging should be highlighted. We would like this bulletin to demonstrate the widespread application of recycled EPS in different industries and establish credibility that it is being used in a variety of interesting recycled-content products. We welcome creative and interesting font treatments and new trends in graphic design.

Target Market(s)

International Government Agencies, Packaging Engineers, Big Box Retailers, & Environmental Professionals

Industry/Entity Type

Plastic Manufacturers

Font styles to use
Sans Serif

Requirements
Must have
• Visual focus points, multiple examples of products and manufacturers as evidence to the information content
Should not have
• Insufficient white space or outdated design elements (like two-tone gradients).

```html
<!DOCTYPE html>
<html lang="en">
<head>
<meta charset="utf-8">
<title>Recycled EPS End Markets</title>
<link rel="stylesheet" href="https://fonts.googleapis.com/css2?family=Montserrat:wght@300;400;500;600;700;800&display=swap">
<style>
:root{
  --olive:#a3a517;
  --gold:#bb8a0e;
  --brown:#5e2b1a;
  --blue:#5e8aa5;
  --orange:#f7a11a;
  --ink:#1e1e1e;
  --muted:#555;
  --stage:#d6d6d6;
  --paper:#ffffff;
}
*{box-sizing:border-box;margin:0;padding:0}
html,body{width:1200px;height:851px;overflow:hidden;background:var(--stage);font-family:"Montserrat",sans-serif;color:var(--ink)}
.page{position:absolute;top:52px;width:527px;height:745px;background:var(--paper);box-shadow:0 2px 6px rgba(0,0,0,.18);overflow:hidden}
.page--left{left:53px}
.page--right{left:623px}
.page__art{position:absolute;left:0;top:0;width:527px;height:745px}
.page__rule{position:absolute;left:0;bottom:0;width:100%;height:3px;background:linear-gradient(90deg,var(--olive) 0 50%,var(--gold) 50% 100%)}
.abs{position:absolute}

.title-light{left:26px;top:10px;font-weight:300;font-size:37px;letter-spacing:17px;color:var(--olive);line-height:1}
.title-bold{left:26px;top:50px;font-weight:800;font-size:24px;color:var(--olive);line-height:1}
.brand{right:28px;top:24px;display:flex;align-items:center;gap:6px}
.brand__dot{width:62px;height:62px;border-radius:50%;background:var(--gold)}
.brand__name{font-weight:600;font-size:12px;line-height:1.15;color:var(--brown)}

.market{width:140px;font-size:7.6px;line-height:12.7px;color:var(--ink)}
.market h3{font-size:9px;font-weight:700;margin-bottom:4px;line-height:1.2}
.market--r{text-align:right}

.stat{left:206px;top:212px;width:80px;height:27px;border:1px solid var(--orange);background:#fff;text-align:center;color:var(--orange)}
.stat b{display:block;font-size:11.5px;font-weight:800;line-height:14px}
.stat b small{font-size:8px}
.stat span{display:block;font-size:3.4px;letter-spacing:.5px;line-height:4.2px;font-weight:700}
.stat-caption{left:220px;top:258px;font-size:3.6px;color:var(--orange);letter-spacing:.3px;font-style:italic}

.band{left:26px;top:368px;width:475px;height:28px;background:var(--olive);color:#fff;font-weight:800;font-size:13.6px;display:flex;align-items:center;justify-content:center}

.core{left:27px;top:485px;width:152px;height:152px;border-radius:50%;display:flex;align-items:center;justify-content:center}
.core__ring{width:130px;height:130px;border-radius:50%;background:#fff;box-shadow:0 3px 10px rgba(0,0,0,.15);display:flex;align-items:center;justify-content:center}
.core__disc{width:100px;height:100px;border-radius:50%;background:var(--gold);color:#fff;font-weight:600;font-size:12px;display:flex;align-items:center;justify-content:center;text-align:center;line-height:1.2}

.app{left:241px;width:250px;height:40px;background:#fff;border-radius:0 20px 20px 0;box-shadow:0 2px 5px rgba(0,0,0,.12);padding:6px 14px 0 42px}
.app h4{font-size:6.8px;font-weight:600;margin-bottom:3px}
.app p{font-size:5.5px;line-height:10px;color:#333}
.app__icon{position:absolute;left:-21px;top:-2px;width:44px;height:44px;border-radius:50%;box-shadow:0 1px 4px rgba(0,0,0,.2);display:flex;align-items:center;justify-content:center}
.app__icon svg{width:20px;height:20px}

.heading{left:26px;top:18px;font-weight:800;font-size:20.5px;line-height:25px;color:var(--gold)}
.heading em{font-style:normal;color:var(--brown)}

.product{width:141px;height:120px;border:1px solid}
.product__photo{position:absolute;left:50%;top:-24px;width:82px;height:82px;margin-left:-41px;border-radius:50%;border:6px solid;background:#fff;display:flex;align-items:center;justify-content:center}
.product__photo i{display:block;width:48px;height:48px;border-radius:50%}
.product__name{position:absolute;left:0;right:0;top:68px;text-align:center;font-weight:700;font-size:11px;line-height:14px}
.product__maker{position:absolute;left:50%;bottom:-9px;width:94px;margin-left:-47px;height:15px;color:#fff;font-size:7px;font-weight:700;display:flex;align-items:center;justify-content:center}

.band--gold{left:0;top:461px;width:527px;height:28px;background:var(--gold);color:#fff;font-weight:800;font-size:11.4px;display:flex;align-items:center;justify-content:center}

.use{width:110px;text-align:center}
.use h5{font-size:8.4px;font-weight:700;line-height:13px;margin-bottom:3px}
.use p{font-size:7.4px;line-height:11.5px;color:var(--muted)}
.drop{width:72px;height:72px;display:flex;align-items:center;justify-content:center}
.drop__inner{width:56px;height:56px;border-radius:50%;border:1px solid rgba(255,255,255,.7);display:flex;align-items:center;justify-content:center}
.drop svg{width:26px;height:26px}
</style>
</head>
<body>

<!-- LEFT PAGE -->
<section class="page page--left">
  <svg class="page__art" viewBox="0 0 527 745" aria-hidden="true">
    <polygon points="0,21 23,42 0,63" fill="var(--olive)"/>
    <circle cx="265" cy="217" r="105" fill="none" stroke="var(--olive)" stroke-width=".7"/>
    <circle cx="265" cy="217" r="78" fill="none" stroke="var(--olive)" stroke-width="9"/>
    <circle cx="265" cy="217" r="67" fill="none" stroke="var(--olive)" stroke-width="1.4"/>
    <polygon points="334,196 344,204 339,207" fill="var(--olive)"/>
    <polygon points="196,238 186,230 191,227" fill="var(--olive)"/>
    <circle cx="340" cy="219" r="2.5" fill="#fff"/>
    <circle cx="190" cy="217" r="2.5" fill="#fff"/>
    <path d="M228,242 Q248,260 274,252" fill="none" stroke="var(--orange)" stroke-width=".8" stroke-dasharray="2 2"/>
    <g stroke-width="3.5" fill="#fff">
      <circle cx="187" cy="138" r="17" stroke="var(--gold)"/>
      <circle cx="341" cy="138" r="17" stroke="var(--olive)"/>
      <circle cx="158" cy="214" r="17" stroke="var(--olive)"/>
      <circle cx="371" cy="214" r="17" stroke="var(--gold)"/>
      <circle cx="190" cy="297" r="17" stroke="var(--gold)"/>
      <circle cx="339" cy="297" r="17" stroke="var(--olive)"/>
    </g>
    <g fill="none" stroke="var(--ink)" stroke-width="1">
      <rect x="180" y="131" width="14" height="14" rx="1"/><line x1="187" y1="131" x2="187" y2="145"/>
      <rect x="335" y="132" width="12" height="12" rx="2"/><line x1="338" y1="138" x2="344" y2="138"/>
      <rect x="151" y="207" width="14" height="14"/><line x1="151" y1="214" x2="165" y2="214"/>
      <path d="M364,220 h14 l-2,-8 h-10 z"/>
      <rect x="184" y="290" width="12" height="14" rx="1"/><line x1="187" y1="295" x2="193" y2="295"/>
      <circle cx="335" cy="294" r="2"/><circle cx="343" cy="294" r="2"/><path d="M331,303 q4,-6 8,0 q4,-6 8,0"/>
    </g>
    <path d="M0,477 A145,145 0 0 0 0,763" fill="none"/>
    <path d="M102,485 A76,76 0 0 0 102,637" fill="none" stroke="var(--gold)" stroke-width="10"/>
    <path d="M178,561 H214 M214,433 V687" fill="none" stroke="var(--ink)" stroke-width=".9" stroke-dasharray="1.2 1.6"/>
    <g fill="none" stroke="var(--ink)" stroke-width=".9" stroke-dasharray="1.2 1.6">
      <path d="M214,433 H233"/><path d="M214,497 H233"/><path d="M214,561 H233"/><path d="M214,624 H233"/><path d="M214,687 H233"/>
    </g>
    <g fill="#fff" stroke="var(--olive)" stroke-width=".9">
      <circle cx="235" cy="433" r="2.6"/><circle cx="235" cy="497" r="2.6"/><circle cx="235" cy="561" r="2.6"/><circle cx="235" cy="624" r="2.6"/><circle cx="235" cy="687" r="2.6"/><circle cx="181" cy="561" r="2.6"/><circle cx="214" cy="561" r="2.6"/>
    </g>
  </svg>

  <div class="abs title-light">RECYLED</div>
  <div class="abs title-bold">EPS END MARKETS</div>
  <div class="abs brand"><span class="brand__dot"></span><span class="brand__name">Foamloop<br>Council</span></div>

  <div class="abs" role="img" aria-label="Photo of a white recycled-content EPS foam cooler" style="left:222px;top:174px;width:96px;height:80px;border-radius:8px 8px 14px 14px;background:linear-gradient(180deg,#f3f3f3,#dcdcdc)"></div>
  <div class="abs stat"><b>30,800 <small>TONS</small></b><span>OF EXPANDED POLYSTYRENE (EPS)<br>WAS RECYCLED IN 2022</span></div>
  <div class="abs stat-caption">RECYCLED CONTENT EPS COOLER</div>

  <div class="abs market market--r" style="left:13px;top:112px"><h3>APPLIANCES</h3>Impact-resistant molded EPS from recycled content for large goods</div>
  <div class="abs market market--r" style="left:-13px;top:188px"><h3>FURNITURE</h3>Re-engineered interior foam components or transport pads</div>
  <div class="abs market market--r" style="left:18px;top:270px"><h3>PHARMACEUTICALS</h3>Cold-chain packaging for vaccines and medications using recycled EPS</div>
  <div class="abs market" style="left:375px;top:112px"><h3>PHARMACEUTICALS</h3>Cold-chain packaging for vaccines and medications using recycled EPS</div>
  <div class="abs market" style="left:401px;top:188px"><h3>FOOD &amp; BEVERAGE</h3>Insulated boxes for seafood and perishables with recycled foam</div>
  <div class="abs market" style="left:369px;top:270px"><h3>CONSUMER ELECTRONICS</h3>Precision-fit protective packaging from recycled EPS</div>

  <div class="abs band">INDUSTRY APPLICATIONS OF RECYCLED EPS MATERIALS</div>

  <div class="abs core"><div class="core__ring"><div class="core__disc">Foamloop<br>Council</div></div></div>

  <div class="abs app" style="top:413px"><span class="app__icon" style="background:var(--olive)"><svg viewBox="0 0 20 20" fill="none" stroke="#fff" stroke-width="1.2"><circle cx="10" cy="7" r="4"/><path d="M3,19 q7,-10 14,0"/></svg></span><h4>CONSTRUCTION &amp; ARCHITECTURAL</h4><p>Walls, insulation, and geofoam are all products that can utiliz recycled EPS as part of the design.</p></div>
  <div class="abs app" style="top:477px"><span class="app__icon" style="background:var(--orange)"><svg viewBox="0 0 20 20" fill="none" stroke="#fff" stroke-width="1.2"><path d="M4,18 V8 h4 v4 h4 V4 h4 v14 z"/></svg></span><h4>TEXTILE &amp; FIBER</h4><p>Specialized techniques produce fine fibers of EPS to be used i non-woven mats and in nanofibers to help absorb oil spills.</p></div>
  <div class="abs app" style="top:541px"><span class="app__icon" style="background:var(--blue)"><svg viewBox="0 0 20 20" fill="none" stroke="#fff" stroke-width="1.2"><path d="M3,14 L14,3 L17,6 L6,17 z M6,11 L9,14"/></svg></span><h4>WOOD COMPOSITES &amp; BLENDS</h4><p>Novel applications using EPS can avoid traditional glue use in wood composites by combining EPS with waste wood fibers.</p></div>
  <div class="abs app" style="top:604px"><span class="app__icon" style="background:var(--brown)"><svg viewBox="0 0 20 20" fill="none" stroke="#fff" stroke-width="1.2"><rect x="4" y="8" width="10" height="10" rx="1"/><path d="M9,8 L16,2"/></svg></span><h4>PAINTS, COATINGS, ADHESIVES</h4><p>Water resistant paints are needed for architectural and roadv applications.</p></div>
  <div class="abs app" style="top:667px"><span class="app__icon" style="background:var(--gold)"><svg viewBox="0 0 20 20" fill="none" stroke="#fff" stroke-width="1.2"><circle cx="12" cy="7" r="4"/><path d="M2,14 q5,-3 9,0 h6"/></svg></span><h4>ADDITIVES</h4><p>Modern approaches to plastics manufacturing can use recycl EPS to create material for 3D printing.</p></div>

  <div class="page__rule"></div>
</section>

<!-- RIGHT PAGE -->
<section class="page page--right">
  <svg class="page__art" viewBox="0 0 527 745" aria-hidden="true">
    <polygon points="0,21 23,42 0,63" fill="var(--olive)"/>
  </svg>
  <div class="abs heading">PRODUCTS MADE WITH<br>RECYCLED EPS AND THEIR<br><em>MANUFACTURERS</em></div>
  <div class="abs brand"><span class="brand__dot"></span><span class="brand__name">Foamloop<br>Council</span></div>

  <div class="abs product" style="left:26px;top:135px;border-color:var(--brown)">
    <div class="product__photo" style="border-color:var(--brown)"><i role="img" aria-label="Photo of a molded foam automotive part" style="background:linear-gradient(135deg,#f1f1f1,#c9c9c9)"></i></div>
    <div class="product__name" style="color:var(--brown);top:64px">Automotive<br>components</div>
    <div class="product__maker" style="background:var(--brown)">By Kestrel Molding</div>
  </div>
  <div class="abs product" style="left:193px;top:135px;border-color:var(--gold)">
    <div class="product__photo" style="border-color:var(--gold)"><i role="img" aria-label="Photo of a blue slatted patio bench" style="background:linear-gradient(135deg,#7f9fb6,#4d6d85)"></i></div>
    <div class="product__name" style="color:var(--gold);top:71px">Patio Bench</div>
    <div class="product__maker" style="background:var(--gold)">BY Alder Lane</div>
  </div>
  <div class="abs product" style="left:359px;top:135px;border-color:var(--olive)">
    <div class="product__photo" style="border-color:var(--olive)"><i role="img" aria-label="Photo of a black plastic spoon" style="background:radial-gradient(#555,#fff 70%)"></i></div>
    <div class="product__name" style="color:var(--olive);top:69px">Spoon</div>
    <div class="product__maker" style="background:var(--olive)">By Greenfork Goods</div>
  </div>

  <div class="abs product" style="left:26px;top:309px;border-color:var(--blue)">
    <div class="product__photo" style="border-color:var(--blue)"><i role="img" aria-label="Photo of a white surfboard blank" style="background:linear-gradient(90deg,#fff,#e8e2d8,#fff)"></i></div>
    <div class="product__name" style="color:var(--blue);top:71px">Picture Frame</div>
    <div class="product__maker" style="background:var(--blue)">By Kestrel Molding</div>
  </div>
  <div class="abs product" style="left:193px;top:309px;border-color:var(--ink)">
    <div class="product__photo" style="border-color:var(--ink)"><i role="img" aria-label="Photo of wooden clothing hangers" style="background:radial-gradient(#a0715a,#fff 72%)"></i></div>
    <div class="product__name" style="color:var(--ink);top:64px">Clothing<br>hangers</div>
    <div class="product__maker" style="background:var(--ink)">BY Alder Lane</div>
  </div>
  <div class="abs product" style="left:359px;top:309px;border-color:var(--brown)">
    <div class="product__photo" style="border-color:var(--orange)"><i role="img" aria-label="Photo of a light wood picture frame" style="border-radius:2px;background:linear-gradient(135deg,#d9cdb8,#bfae92)"></i></div>
    <div class="product__name" style="color:var(--orange);top:68px">Surfboard<br>blanks</div>
    <div class="product__maker" style="background:var(--orange)">By Greenfork Goods</div>
  </div>

  <div class="abs band--gold">INNOVATIVE USES FOR RECYCLED EPS MATERIALS</div>

  <div class="abs use" style="left:123px;top:512px"><h5>Automatic Emotion<br>Analysis</h5><p>Gain insights into the emotions of your employees interactions</p></div>
  <div class="abs use" style="left:293px;top:512px"><h5>Automatic Emotion<br>Analysis</h5><p>Gain insights into the emotions of your employees interactions</p></div>
  <div class="abs use" style="left:37px;top:659px"><h5>Automatic Emotion<br>Analysis</h5><p>Gain insights into the emotions of your employees interactions</p></div>
  <div class="abs use" style="left:205px;top:662px"><h5>Automatic Emotion<br>Analysis</h5><p>Gain insights into the emotions of your employees interactions</p></div>
  <div class="abs use" style="left:375px;top:662px"><h5>Automatic Emotion<br>Analysis</h5><p>Gain insights into the emotions of your employees interactions</p></div>

  <div class="abs drop" style="left:60px;top:574px;border-radius:50%;background:var(--olive)"><div class="drop__inner"><svg viewBox="0 0 26 26" fill="none" stroke="#fff" stroke-width="2"><circle cx="9" cy="9" r="5"/><circle cx="17" cy="17" r="5"/><line x1="21" y1="21" x2="25" y2="25"/></svg></div></div>
  <div class="abs drop" style="left:142px;top:574px;border-radius:0 50% 50% 50%;background:var(--orange)"><div class="drop__inner"><svg viewBox="0 0 26 26" fill="none" stroke="#fff" stroke-width="2.4"><path d="M6,13 a7,7 0 1 1 7,7"/><polyline points="3,10 6,14 10,11"/></svg></div></div>
  <div class="abs drop" style="left:227px;top:574px;border-radius:50% 50% 50% 0;background:var(--brown)"><div class="drop__inner"><svg viewBox="0 0 26 26" fill="none" stroke="#fff" stroke-width="2.4"><path d="M6,13 a7,7 0 1 1 7,7"/><polyline points="3,10 6,14 10,11"/></svg></div></div>
  <div class="abs drop" style="left:312px;top:574px;border-radius:0 50% 50% 50%;background:var(--blue)"><div class="drop__inner"><svg viewBox="0 0 26 26" fill="none" stroke="#fff" stroke-width="2.4"><path d="M6,13 a7,7 0 1 1 7,7"/><polyline points="3,10 6,14 10,11"/></svg></div></div>
  <div class="abs drop" style="left:399px;top:574px;border-radius:50% 50% 50% 0;background:var(--gold)"><div class="drop__inner"><svg viewBox="0 0 26 26" fill="none" stroke="#fff" stroke-width="2.4"><path d="M6,13 a7,7 0 1 1 7,7"/><polyline points="3,10 6,14 10,11"/></svg></div></div>

  <div class="page__rule"></div>
</section>

</body>
</html>
```